Quorvane.com home page upgrade. Strong existing assets.

We are looking to redesign our homepage. We need to communicate three large concepts.

1) Software-as-a-Service for connected electronic device management
2) Mesh-Networking-as-a-Service allows local devices to talk together easily
3) We have 3 pieces of hardware:
A) T7 Badger
B) T7 Owl
C) T7 Salamander

We will keep the color scheme, although we would like the general feel to be lighter than our current page at http://quorvane.example

See the word doc for more details.

Requirements
Nice to have
• large images, modern design

```html
<!DOCTYPE html>
<html lang="en">
<head>
<meta charset="utf-8">
<title>Quorvane — Your Professional Internet-of-Things Solution</title>
<link rel="stylesheet" href="https://fonts.googleapis.com/css2?family=Lato:ital,wght@0,400;0,700;0,900;1,400&display=swap">
<style>
  :root {
    --white: #ffffff;
    --ink: #2a2226;
    --nav-ink: #3a2a2f;
    --brand-dark: #3b2228;
    --hero: #834854;
    --hero-device: #6d3e49;
    --plum: #6a3d48;
    --orange: #f28b31;
    --band: #f3f2f2;
  }
  * { box-sizing: border-box; margin: 0; padding: 0; }
  html, body { width: 1200px; height: 1000px; overflow: hidden; background: var(--white); }
  body { position: relative; font-family: "Lato", sans-serif; color: var(--ink); }

  .site-header { position: absolute; top: 0; left: 0; width: 1200px; height: 98px; background: var(--white); }
  .brand { position: absolute; left: 208px; top: 31px; font-size: 34px; font-weight: 900; color: var(--brand-dark); letter-spacing: -0.5px; line-height: 1; }
  .main-nav { position: absolute; top: 48px; left: 416px; display: flex; gap: 0; }
  .main-nav a { font-size: 10.5px; font-weight: 700; letter-spacing: 0.4px; color: var(--nav-ink); text-decoration: none; text-transform: uppercase; position: absolute; white-space: nowrap; }

  .hero { position: absolute; top: 98px; left: 0; width: 1200px; height: 409px; background: var(--hero); overflow: hidden; }
  .hero-devices { position: absolute; left: 313px; top: 117px; width: 574px; height: 292px; background: var(--hero-device); border-radius: 6px 6px 0 0; }
  .hero-title { position: absolute; top: 50px; left: 0; width: 1200px; text-align: center; color: var(--white); font-size: 40px; font-weight: 700; letter-spacing: 2px; line-height: 48px; text-shadow: 0 2px 3px rgba(0,0,0,0.25); }
  .hero-tagline { position: absolute; top: 150px; left: 0; width: 1200px; text-align: center; color: var(--white); font-size: 20px; font-style: italic; letter-spacing: 1.5px; }
  .btn { position: absolute; top: 230px; height: 48px; display: flex; align-items: center; justify-content: center; color: var(--white); font-size: 18px; font-weight: 900; text-transform: uppercase; text-decoration: none; letter-spacing: 0.3px; }
  .btn-secondary { left: 309px; width: 271px; background: var(--plum); }
  .btn-primary { left: 619px; width: 272px; background: var(--orange); }

  .intro-heading { position: absolute; top: 566px; left: 0; width: 1200px; text-align: center; font-size: 31px; font-weight: 700; letter-spacing: 2.5px; line-height: 44px; text-transform: uppercase; color: var(--ink); }
  .brand-large { position: absolute; top: 700px; left: 0; width: 1200px; text-align: center; font-size: 76px; font-weight: 900; color: var(--brand-dark); letter-spacing: -1px; line-height: 1; }

  .audience-links { position: absolute; top: 836px; left: 208px; }
  .audience-card { position: absolute; top: 0; width: 250px; height: 79px; background: var(--plum); color: var(--white); display: flex; align-items: center; justify-content: center; text-align: center; font-size: 19px; font-weight: 700; line-height: 29px; text-transform: uppercase; text-decoration: none; }

  .next-band { position: absolute; top: 987px; left: 100px; width: 1000px; height: 13px; background: var(--band); }
</style>
</head>
<body>
  <header class="site-header">
    <div class="brand">Quorvane</div>
    <nav class="main-nav">
      <a href="#" style="left:0">Manufacturers</a>
      <a href="#" style="left:107px">Technology Integrators</a>
      <a href="#" style="left:268px">Enterprise Plans</a>
      <a href="#" style="left:388px">T7 Devices</a>
      <a href="#" style="left:473px">About</a>
      <a href="#" style="left:524px">Contact</a>
    </nav>
  </header>

  <section class="hero">
    <div class="hero-devices" role="img" aria-label="Illustration of a laptop, tablet and phone showing the platform"></div>
    <h1 class="hero-title">Your Professional<br>“Internet-of-Things” Solution</h1>
    <p class="hero-tagline">– Today –</p>
    <a class="btn btn-secondary" href="#">How does it work?</a>
    <a class="btn btn-primary" href="#">Check our plans</a>
  </section>

  <h2 class="intro-heading">Quorvane, a scalable, secure, full-stack<br>M2M solution on web &amp; mobile</h2>
  <div class="brand-large">Quorvane</div>

  <nav class="audience-links">
    <a class="audience-card" href="#" style="left:0">Quorvane for<br>OEM’s</a>
    <a class="audience-card" href="#" style="left:267px">Quorvane for<br>Tech Integrators</a>
    <a class="audience-card" href="#" style="left:534px">Quorvane Enterprise<br>for Companies</a>
  </nav>

  <div class="next-band"></div>
</body>
</html>
```